Brava Nest (Smart Home, Installation, Repair Industry) (Contest)

Looking for a website design for my company
Services we offer:
Phone Repair
TV Mounting
Security Camera Installation
Networking / Wi-Fi
Smart Home Services
IT Support

Looking for a website similar to trovely.example

Few tabs
About Us
Contact Us
Areas Served
Pricing and Services

```html
<!DOCTYPE html>
<html lang="en">
<head>
<meta charset="utf-8">
<title>Brava Nest — Smart Home, Installation, Repair</title>
<link href="https://fonts.googleapis.com/css2?family=Montserrat:wght@600;700;800&family=Oswald:wght@300;400&family=Lato:ital,wght@0,400;0,700;1,400&display=swap" rel="stylesheet">
<style>
:root{
  --orange:#f7941d;
  --orange-soft:#f9a845;
  --orange-pale:#fbc98a;
  --ink:#111111;
  --text:#444444;
  --muted:#8a8a8a;
  --light:#f1f2f4;
  --white:#ffffff;
  --hero:#2b2b2b;
}
*{margin:0;padding:0;box-sizing:border-box}
html,body{width:1200px;height:3208px;overflow:hidden;background:var(--white)}
body{position:relative;font-family:"Lato",sans-serif;color:var(--text)}
.abs{position:absolute}
.brand{font-family:"Montserrat",sans-serif;font-weight:800;color:var(--orange);font-size:46px;letter-spacing:-1px}
.head-stripe{left:0;top:0;width:1200px;height:5px;background:var(--orange)}
.social-tab{left:953px;top:0;width:247px;height:40px;background:var(--orange);clip-path:polygon(0 0,100% 0,100% 100%,28px 100%)}
.social-tab span{position:absolute;top:0;width:1px;height:40px;background:rgba(255,255,255,.4)}
.nav{top:72px;left:371px;display:flex;gap:25px;font-size:15px;color:var(--muted)}
.nav .active{color:var(--orange);position:relative}
.nav .active:before{content:"";position:absolute;left:0;right:0;top:-16px;height:2px;background:var(--orange)}
.head-phone{left:980px;top:70px;font-family:"Oswald",sans-serif;font-size:24px;color:var(--ink)}
.divider-v{width:1px;height:46px;background:#ddd;top:62px}
.hero{left:0;top:125px;width:1200px;height:573px;background:linear-gradient(100deg,#1d1d1d 0%,#3a3633 45%,#2f2f2f 62%,#545454 78%,#2a2a2a 100%)}
.hero h1{left:267px;top:476px;font-family:"Montserrat",sans-serif;font-weight:700;font-size:45px;color:var(--orange);letter-spacing:1px}
.hero p{left:267px;top:540px;width:560px;font-style:italic;font-size:16px;line-height:29px;color:#eee}
.arrow{top:548px;width:41px;height:41px;border:1px solid #ccc;display:flex;align-items:center;justify-content:center}
.what{left:0;top:698px;width:1200px;height:479px;background:var(--orange)}
.section-title{font-family:"Montserrat",sans-serif;font-weight:800;font-size:36px;color:var(--ink);line-height:42px}
.grid{left:498px;top:770px;width:627px;height:334px;display:grid;grid-template-columns:repeat(3,209px);grid-template-rows:repeat(2,167px)}
.cell{border:1px solid rgba(255,255,255,.35);display:flex;flex-direction:column;align-items:center;justify-content:flex-start;padding-top:22px;font-family:"Oswald",sans-serif;font-weight:300;font-size:20px;color:var(--white);text-align:center;line-height:28px}
.cell svg{margin-bottom:10px}
.cell.lite{background:var(--orange-soft)}
.frame{left:77px;top:916px;width:313px;height:386px;border:8px solid var(--orange-pale);background:var(--white)}
.worker{left:118px;top:866px;width:318px;height:436px;background:linear-gradient(180deg,#f2e5d8 0%,#2e4a63 35%,#1f3a52 80%,#aab0b6 100%);border-radius:60px 60px 0 0}
.cta{left:390px;top:1177px;width:810px;height:125px;background:var(--light)}
.cta p{left:500px;top:1207px;font-family:"Oswald",sans-serif;font-weight:300;font-size:25px;line-height:34px;color:#555;text-transform:uppercase}
.btn{display:flex;align-items:center;justify-content:center;font-family:"Montserrat",sans-serif;font-weight:600;font-size:17px;color:var(--white);background:var(--orange);border-radius:3px}
.btn.dark{background:var(--ink)}
.copy{font-size:14px;line-height:26px;color:var(--muted)}
.orange{color:var(--orange)}
.about-bg{left:77px;top:1738px;width:313px;height:314px;background:var(--light)}
.about-photo{left:390px;top:1636px;width:810px;height:416px;background:linear-gradient(110deg,#7b6a58 0%,#c9c2b8 35%,#e9e9e9 60%,#f6f6f6 100%)}
.about-card{left:130px;top:1688px;width:416px;height:312px;background:var(--white);box-shadow:0 4px 24px rgba(0,0,0,.12);padding:50px 42px}
.about-card h3{font-family:"Oswald",sans-serif;font-weight:300;font-size:30px;color:var(--ink);margin-bottom:22px}
.ring{border-radius:50%}
.footer{left:0;top:2667px;width:1200px;height:469px;background:var(--light)}
.f-item{left:121px;font-size:14px;line-height:26px;color:#666}
.sq{top:3012px;width:47px;height:47px;background:var(--white);box-shadow:0 2px 8px rgba(0,0,0,.06)}
.bottom{left:0;top:3136px;width:1200px;height:72px;background:var(--orange);display:flex;align-items:center;justify-content:center;font-size:13px;color:var(--white);gap:14px}
</style>
</head>
<body>

<header>
  <div class="abs head-stripe"></div>
  <div class="abs social-tab"><span style="left:67px"></span><span style="left:127px"></span><span style="left:187px"></span></div>
  <div class="abs brand" style="left:77px;top:30px">Brava Nest</div>
  <nav class="abs nav">
    <span class="active">Home</span><span>About Us</span><span>Area Served</span><span>Pricing &amp; srvices</span><span>Contact Us</span>
    <svg width="20" height="20" viewBox="0 0 20 20" fill="none" stroke="#222" stroke-width="1.8"><circle cx="8" cy="8" r="6"/><path d="M12.5 12.5L18 18"/></svg>
  </nav>
  <div class="abs divider-v" style="left:920px"></div>
  <svg class="abs" style="left:940px;top:64px" width="30" height="40" viewBox="0 0 30 40" fill="none" stroke="#f7941d" stroke-width="2"><rect x="2" y="8" width="17" height="30" rx="3"/><path d="M7 33h7"/><path d="M22 8a6 6 0 0 1 3 5M24 3a11 11 0 0 1 5 9"/></svg>
  <div class="abs head-phone">123.456.7890</div>
  <div class="abs divider-v" style="left:1122px"></div>
</header>

<section class="abs hero" role="img" aria-label="Dark interior photo with a wall-mounted smart thermostat"></section>
<h1 class="abs hero-title" style="left:267px;top:476px;font-family:'Montserrat',sans-serif;font-weight:700;font-size:45px;color:var(--orange);letter-spacing:1px">LOREM IPSUM DOLOR</h1>
<p class="abs" style="left:267px;top:540px;width:560px;font-style:italic;font-size:16px;line-height:29px;color:#eee">Lorem ipsum dolor sit amet, consectetur adipiscing elit, sed do eiusmod tempor incididunt ut labore et dolore magna aliqua.</p>
<div class="abs arrow" style="left:1029px"><svg width="12" height="16" viewBox="0 0 12 16" fill="none" stroke="#fff" stroke-width="2"><path d="M9 2L3 8l6 6"/></svg></div>
<div class="abs arrow" style="left:1082px"><svg width="12" height="16" viewBox="0 0 12 16" fill="none" stroke="#f7941d" stroke-width="2"><path d="M3 2l6 6-6 6"/></svg></div>

<section class="abs what"></section>
<h2 class="abs section-title" style="left:80px;top:768px;color:var(--white)">WHAT WE DO</h2>
<div class="abs grid">
  <div class="cell"><svg width="76" height="74" viewBox="0 0 76 74" fill="none" stroke="#fff" stroke-width="2"><path d="M4 36L26 14l22 22M10 30v30h30V30"/><rect x="20" y="42" width="10" height="18"/><rect x="42" y="26" width="30" height="44" rx="3"/><path d="M50 46a9 9 0 0 1 14 0M53 50a5 5 0 0 1 8 0"/></svg>Smart Home Services</div>
  <div class="cell lite"><svg width="76" height="74" viewBox="0 0 76 74" fill="none" stroke="#fff" stroke-width="2"><rect x="4" y="14" width="54" height="38" rx="2"/><path d="M4 44h54M24 52l-3 10h20l-3-10M14 62h34"/><rect x="60" y="6" width="12" height="30" rx="2"/><path d="M64 12h4M64 18h4M64 24h4"/></svg>TV Mounting</div>
  <div class="cell"><svg width="76" height="74" viewBox="0 0 76 74" fill="none" stroke="#fff" stroke-width="2"><circle cx="38" cy="37" r="13"/><circle cx="38" cy="8" r="5"/><circle cx="38" cy="66" r="5"/><circle cx="10" cy="37" r="5"/><circle cx="66" cy="37" r="5"/><circle cx="18" cy="17" r="5"/><circle cx="58" cy="17" r="5"/><circle cx="18" cy="57" r="5"/><circle cx="58" cy="57" r="5"/><path d="M33 44V30l10 14V30"/></svg>Networking / Wi-Fi</div>
  <div class="cell lite"><svg width="76" height="74" viewBox="0 0 76 74" fill="none" stroke="#fff" stroke-width="2"><circle cx="24" cy="26" r="9"/><circle cx="24" cy="26" r="17" stroke-dasharray="6 4"/><rect x="38" y="14" width="32" height="56" rx="4"/><path d="M48 62h12"/></svg>Phone Repair</div>
  <div class="cell"><svg width="76" height="74" viewBox="0 0 76 74" fill="none" stroke="#fff" stroke-width="2"><rect x="6" y="8" width="56" height="20" rx="10"/><circle cx="56" cy="18" r="5"/><path d="M20 28v16h20v10h8V38"/><rect x="34" y="54" width="14" height="14" rx="2"/></svg>Security Camera<br>Installation</div>
  <div class="cell lite"><svg width="76" height="74" viewBox="0 0 76 74" fill="none" stroke="#fff" stroke-width="2"><rect x="4" y="8" width="68" height="44" rx="2"/><path d="M30 52l-3 12h22l-3-12M20 66h36"/><circle cx="24" cy="22" r="6"/><path d="M14 44a10 10 0 0 1 20 0M46 16l14 14M56 14l6 6"/></svg>IT Support</div>
</div>
<div class="abs frame"></div>
<div class="abs worker" role="img" aria-label="Photo of a smiling technician in a navy uniform and cap holding a laptop"></div>

<div class="abs cta"></div>
<p class="abs" style="left:500px;top:1207px;font-family:'Oswald',sans-serif;font-weight:300;font-size:25px;line-height:34px;color:#555">LOOKING FOR SMART HOME, INSTALLATION,<br>REPAIR INDUSTRY...?</p>
<div class="abs btn dark" style="left:936px;top:1214px;width:187px;height:52px">CALL US TODAY</div>

<h2 class="abs section-title" style="left:80px;top:1371px">WELCOME TO<br><span class="orange">BRAVA NEST</span></h2>
<p class="abs copy" style="left:434px;top:1371px;width:675px">Lorem ipsum dolor sit amet, consectetur adipiscing elit, sed do eiusmod tempor incididunt ut labore et dolore magna aliqua. Ut enim ad minim veniam, quis nostrud exercitation ullamco laboris nisi ut aliquip ex ea commodo consequat. Duis aute irure dolor in reprehenderit in voluptate velit esse cillum dolore eu fugiat nulla pariatur. Excepteur sint occaecat cupidatat non proident.</p>
<div class="abs btn" style="left:432px;top:1505px;width:187px;height:52px">EXPLORE MORE</div>

<div class="abs about-bg"></div>
<div class="abs about-photo" role="img" aria-label="Photo of a finger touching a white smart home wall panel"></div>
<div class="abs about-card">
  <h3>About Brava Nest</h3>
  <p class="copy">Lorem ipsum dolor sit amet, consectetur adipiscing elit, sed do eiusmod tempor incididunt ut labore et dolore magna aliqua. Ut enim ad minim veniam, qu is nostrud exercitation ullamco laboris nisi ut aliqu ip ex ea commodo consequat. Duis aute irure dolor in reprehenderit in voluptate.</p>
</div>

<div class="abs ring" style="left:78px;top:2126px;width:466px;height:466px;border:2px solid #eeeeee"></div>
<div class="abs ring" style="left:100px;top:2148px;width:422px;height:422px;border:5px solid #e8e8e8"></div>
<div class="abs ring" style="left:124px;top:2172px;width:374px;height:374px;border:8px solid #dcdcdc"></div>
<div class="abs ring" style="left:140px;top:2188px;width:342px;height:342px;background:radial-gradient(circle at 45% 40%,#e2b08a 0%,#5a5a8c 35%,#2e3565 70%,#1d2347 100%)" role="img" aria-label="Photo of a hand holding a phone with a glowing Wi-Fi network graphic"></div>
<div class="abs ring" style="left:390px;top:2392px;width:196px;height:196px;background:var(--white)"></div>
<div class="abs ring" style="left:396px;top:2398px;width:184px;height:184px;background:radial-gradient(circle at 60% 40%,#f7b25a,#e98a1a)" role="img" aria-label="Orange-toned photo of technicians at work"></div>

<h2 class="abs section-title" style="left:679px;top:2196px">PRICING &amp; <span class="orange">SERVICES</span></h2>
<p class="abs" style="left:679px;top:2266px;width:430px;font-style:italic;font-size:16px;line-height:26px;color:#555">Lorem ipsum dolor sit amet, consectetur adipiscing elit, sed aliqua. Ut enim ad minim veniam.</p>
<p class="abs copy" style="left:679px;top:2328px;width:430px">Lorem ipsum dolor sit amet, consectetur adipiscing elit, sed do eiusmod tempor incididunt ut labore et dolore magna aliqua. Ut enim ad minim veniam, quis nostrud exercitation ullamco laboris nisi ut aliquip ex ea commodo consequat.</p>
<div class="abs btn" style="left:677px;top:2465px;width:155px;height:52px">GET PRICING</div>

<footer>
  <div class="abs footer"></div>
  <div class="abs brand" style="left:77px;top:2740px">Brava Nest</div>
  <svg class="abs" style="left:80px;top:2838px" width="14" height="20" viewBox="0 0 14 20" fill="#f7941d"><path d="M7 0a7 7 0 0 0-7 7c0 5 7 13 7 13s7-8 7-13a7 7 0 0 0-7-7zm0 10a3 3 0 1 1 0-6 3 3 0 0 1 0 6z"/></svg>
  <p class="abs f-item" style="top:2834px;width:220px">123, Address, State Name, City Name, Zipcode</p>
  <svg class="abs" style="left:78px;top:2905px" width="20" height="20" viewBox="0 0 20 20" fill="#f7941d"><path d="M4 1l4 4-2 3c1 3 3 5 6 6l3-2 4 4-3 3C8 19 1 12 1 4z"/></svg>
  <p class="abs f-item" style="top:2902px;font-size:16px;color:#333">123.456.7890</p>
  <svg class="abs" style="left:78px;top:2950px" width="20" height="15" viewBox="0 0 20 15" fill="#f7941d"><rect width="20" height="15" rx="1"/><path d="M1 1l9 7 9-7" stroke="#fff" stroke-width="1.5" fill="none"/></svg>
  <p class="abs f-item" style="top:2944px;font-size:16px;color:#333">services@bravanest.example</p>
  <div class="abs sq" style="left:78px"></div>
  <div class="abs sq" style="left:140px"></div>
  <div class="abs sq" style="left:202px"></div>
  <div class="abs" style="left:483px;top:2739px;width:638px;height:320px;background:radial-gradient(ellipse at 50% 50%,#d4d4d4 0%,#e4e4e4 55%,rgba(241,242,244,0) 75%)" role="img" aria-label="Dotted world map"></div>
  <div class="abs" style="left:601px;top:2810px;width:56px;height:50px;background:var(--ink);border-radius:3px"></div>
  <svg class="abs" style="left:621px;top:2820px" width="16" height="22" viewBox="0 0 14 20" fill="#f7941d"><path d="M7 0a7 7 0 0 0-7 7c0 5 7 13 7 13s7-8 7-13a7 7 0 0 0-7-7zm0 10a3 3 0 1 1 0-6 3 3 0 0 1 0 6z"/></svg>
  <div class="abs" style="left:657px;top:2820px;width:353px;height:36px;background:var(--white);font-size:14px;color:#444;display:flex;align-items:center;padding-left:21px">123, Address, State Name, City Name, Zipcode</div>
  <div class="abs bottom"><span>© Copyright Brava Nest - 2020 . All Right Reserved.</span><span>Privacy Policy</span><span>.</span><span>Terms &amp; Conditions</span></div>
</footer>

</body>
</html>
```